Business Createrer

Design an info-graphic which explains the process of what I do to help people and busnesses (Hotels, venues etc) divine a food and Beverage plan for success.

I have an existing website which shows the style I would like to use visit www.glenmarbury.com.au.

I have attached a PPTX showing the 4 components required and then a second page for the process and a copy of the logo and splash images.

I this works I have further design projects including promo videos for apps

Target Market(s)

Food and Beverage industry including hotels, venues, caterers and restaurants

Industry/Entity Type

Business Consultant

Font styles to use
Other font styles liked:
• sweet sans

Requirements
Must have
• icon creations and clear workflow

```html
<!DOCTYPE html>
<html lang="en">
<head>
<meta charset="utf-8">
<title>Glen Marbury – Food &amp; Beverage Concepts</title>
<link href="https://fonts.googleapis.com/css2?family=Arimo:ital,wght@0,400;0,700;1,700&display=swap" rel="stylesheet">
<style>
:root{
  --blue:#2f8fd6;
  --blue-band:#3d8fd1;
  --blue-ring:#4a93d3;
  --navy:#123a66;
  --ink:#222222;
  --grey-bg:#eeeeee;
  --label-bg:#efefef;
  --white:#ffffff;
  --ring:#c9dcef;
  --cup-red:#e8343f;
  --table-blue:#bfe6f8;
}
*{margin:0;padding:0;box-sizing:border-box}
html,body{width:1200px;height:3557px;overflow:hidden;background:var(--white)}
body{position:relative;font-family:"Arimo",Arial,sans-serif;color:var(--ink)}

/* header */
.site-header{position:absolute;left:0;top:0;width:1200px;height:171px}
.brand-name{position:absolute;left:48px;top:22px;color:var(--blue);font-weight:400;font-size:40px;letter-spacing:14px;line-height:62px}
.social{position:absolute;right:40px;top:57px;display:flex;gap:18px}
.social span{width:56px;height:56px;border-radius:50%;background:var(--blue)}

/* hero */
.hero{position:absolute;left:0;top:171px;width:1200px;height:529px;
  background:linear-gradient(120deg,#dfeaf6 0%,#5f9fd8 30%,#e9eef4 52%,#f4c36a 70%,#c8402f 86%,#e8eef5 100%)}

/* quote */
.quote-band{position:absolute;left:0;top:700px;width:1200px;height:142px;background:var(--blue);text-align:center;padding:28px 40px 0}
.quote-band p{color:var(--white);font-size:21px;line-height:31px;text-transform:uppercase}
.quote-band cite{display:block;margin-top:8px;color:var(--navy);font-style:italic;font-weight:700;font-size:17px}

/* about */
.about{position:absolute;left:0;top:842px;width:1200px;height:313px}
.about h2{position:absolute;left:32px;top:64px;color:var(--blue);font-size:38px;font-weight:700}
.about p{position:absolute;left:32px;top:126px;width:680px;font-size:17px;line-height:27px}
.about-photo{position:absolute;left:766px;top:43px;width:403px;height:213px;border:6px solid #b5b5b5;
  background:linear-gradient(90deg,#9a9a9a,#3a3a3a 35%,#1d2a4a 55%,#7a7a7a 80%,#cfcfcf)}

/* components */
.components{position:absolute;left:0;top:1155px;width:1200px;height:885px;background:var(--grey-bg)}
.components > svg{position:absolute;left:0;top:0}
.component{position:absolute;width:290px;text-align:center;color:var(--white)}
.component-icon{display:block;margin:0 auto 8px}
.component h3{font-size:18px;font-weight:700;text-transform:uppercase;margin-bottom:8px}
.component p{font-size:15px;line-height:24px}
.dining-scene{position:absolute;left:411px;top:240px;width:340px;height:340px;border-radius:50%;
  background:radial-gradient(circle at 50% 55%,#ffffff 0%,#ffffff 38%,#d9e9f7 62%,#a9cdec 100%)}

/* steps */
.steps-band{position:absolute;left:0;top:2040px;width:1200px;height:107px;background:var(--blue-band);color:var(--white);
  font-weight:700;font-size:28px;text-transform:uppercase;padding:34px 0 0 284px}
.steps{position:absolute;left:0;top:2147px;width:1200px;height:1150px}
.steps > svg{position:absolute;left:0;top:0}
.step-num{position:absolute;color:var(--blue);font-size:88px;line-height:88px;font-weight:400}
.step-label{position:absolute;background:var(--label-bg);font-size:17px;line-height:25px;padding:12px 16px;color:var(--ink)}
.people-scene{position:absolute;left:415px;top:142px;width:403px;height:301px;border-radius:30px;
  background:radial-gradient(ellipse at 50% 55%,#ffffff 0%,#ffffff 35%,#d9e9f7 65%,#b7d6ef 100%)}

/* footer */
.site-footer{position:absolute;left:0;top:3297px;width:1200px;height:260px;background:var(--blue-band);color:var(--white);text-align:center}
.roles{padding-top:68px;font-weight:700;font-size:21px;line-height:33px;text-transform:uppercase}
.divider{width:747px;height:1px;background:rgba(255,255,255,.6);margin:16px auto 0}
.contacts{display:flex;justify-content:center;gap:40px;margin-top:20px;font-size:16px;text-transform:uppercase}
.contacts span{display:flex;align-items:center;gap:8px}
.icon-defs{position:absolute;width:0;height:0}
</style>
</head>
<body>

<svg class="icon-defs" aria-hidden="true">
  <defs>
    <symbol id="icon-cup" viewBox="0 0 60 80">
      <line x1="34" y1="20" x2="44" y2="2" stroke="#f4a6ae" stroke-width="5" stroke-linecap="round"/>
      <rect x="7" y="16" width="46" height="8" rx="3" fill="#ffffff"/>
      <polygon points="10,24 50,24 45,76 15,76" fill="#e8343f"/>
      <polygon points="10,24 50,24 49,32 11,32" fill="#c92631"/>
    </symbol>
    <symbol id="icon-pot" viewBox="0 0 90 80">
      <circle cx="30" cy="30" r="10" fill="#7cc243"/>
      <circle cx="44" cy="24" r="11" fill="#e8343f"/>
      <circle cx="58" cy="30" r="10" fill="#f2b233"/>
      <circle cx="46" cy="34" r="9" fill="#5aa832"/>
      <rect x="8" y="38" width="74" height="8" rx="3" fill="#e8343f"/>
      <rect x="14" y="46" width="62" height="30" rx="4" fill="#ffffff"/>
      <rect x="14" y="54" width="62" height="5" fill="#e8343f"/>
    </symbol>
    <symbol id="icon-table" viewBox="0 0 100 80">
      <polygon points="18,30 92,30 80,46 6,46" fill="#bfe6f8"/>
      <rect x="12" y="46" width="5" height="28" fill="#bfe6f8"/>
      <rect x="72" y="46" width="5" height="28" fill="#bfe6f8"/>
      <ellipse cx="34" cy="37" rx="8" ry="4" fill="#ffffff"/>
      <ellipse cx="60" cy="37" rx="8" ry="4" fill="#ffffff"/>
      <rect x="46" y="16" width="5" height="18" rx="2" fill="#1f4d7a"/>
      <rect x="84" y="14" width="6" height="36" fill="#ffffff"/>
      <rect x="84" y="30" width="14" height="5" fill="#ffffff"/>
    </symbol>
  </defs>
</svg>

<header class="site-header">
  <div class="brand-name">GLEN<br>MARBURY</div>
  <div class="social"><span></span><span></span><span></span><span></span><span></span></div>
</header>

<div class="hero" role="img" aria-label="Splash image: pizza, red drink cup with straw and a burger against blue liquid splashes"></div>

<section class="quote-band">
  <p>“Food and beverage are only two ingredients to a great food and beverage delivery. Creating culinary experiences are imperative to creating memorable events”</p>
  <cite>GLEN MARBURY</cite>
</section>

<section class="about">
  <h2>About Glen</h2>
  <p>Glen's Strategic Mission, To Effectively Create A Professional Australian Catering Events Industry, Has Always Been His Driving Force</p>
  <div class="about-photo" role="img" aria-label="Portrait photo of the consultant in a suit, in a black and white collage"></div>
</section>

<section class="components">
  <svg width="1200" height="885" viewBox="0 0 1200 885">
    <g stroke="#3f8fd4" stroke-width="34">
      <line x1="581" y1="410" x2="202" y2="244"/>
      <line x1="581" y1="410" x2="1015" y2="244"/>
      <line x1="581" y1="410" x2="202" y2="624"/>
      <line x1="581" y1="410" x2="1015" y2="624"/>
    </g>
    <circle cx="581" cy="410" r="196" fill="#fff" stroke="#4a93d3" stroke-width="10"/>
    <g>
      <circle cx="202" cy="244" r="178" fill="#fff" stroke="var(--ring)" stroke-width="3"/>
      <circle cx="202" cy="244" r="162" fill="#4b93d2"/>
      <circle cx="1015" cy="244" r="178" fill="#fff" stroke="var(--ring)" stroke-width="3"/>
      <circle cx="1015" cy="244" r="162" fill="#4b93d2"/>
      <circle cx="202" cy="624" r="178" fill="#fff" stroke="var(--ring)" stroke-width="3"/>
      <circle cx="202" cy="624" r="162" fill="#4b93d2"/>
      <circle cx="1015" cy="624" r="178" fill="#fff" stroke="var(--ring)" stroke-width="3"/>
      <circle cx="1015" cy="624" r="162" fill="#4b93d2"/>
    </g>
  </svg>
  <div class="dining-scene" role="img" aria-label="Illustration of two diners seated at a table with wine"></div>

  <div class="component" style="left:57px;top:118px">
    <svg class="component-icon" width="62" height="82" role="img" aria-label="Drink cup icon"><use href="#icon-cup"/></svg>
    <h3>Beverage</h3>
    <p>Think of all kinds of drinks from cocktails, wines, beers and soft drinks</p>
  </div>
  <div class="component" style="left:870px;top:118px">
    <svg class="component-icon" width="92" height="82" role="img" aria-label="Cooking pot with food icon"><use href="#icon-pot"/></svg>
    <h3>Food</h3>
    <p>Think of all different kinds of food from breakfast, lunch to fancy dinners, and even snacks</p>
  </div>
  <div class="component" style="left:57px;top:502px">
    <svg class="component-icon" width="100" height="80" role="img" aria-label="Restaurant table icon"><use href="#icon-table"/></svg>
    <h3>Environment</h3>
    <p>Think of all the different kinds of place to eat and drink from restaurants, to cafes, to bars</p>
  </div>
  <div class="component" style="left:870px;top:514px">
    <svg class="component-icon" width="100" height="80" role="img" aria-label="Set table icon"><use href="#icon-table"/></svg>
    <h3>Brand</h3>
    <p>What makes the place distinctive: think Burger Barn to Starfield</p>
  </div>
</section>

<div class="steps-band">Steps of making a new dining concept</div>

<section class="steps">
  <div class="people-scene" role="img" aria-label="Illustration of two diners at a table with wine and food"></div>
  <svg width="1200" height="1150" viewBox="0 0 1200 1150">
    <defs>
      <marker id="arrow-head" viewBox="0 0 10 10" refX="5" refY="5" markerWidth="3.2" markerHeight="3.2" orient="auto">
        <path d="M0,0 L10,5 L0,10 z" fill="#4a93d3"/>
      </marker>
    </defs>
    <g stroke="#4a93d3" stroke-width="8">
      <line x1="166" y1="332" x2="142" y2="225"/>
      <line x1="166" y1="332" x2="273" y2="232"/>
      <line x1="166" y1="332" x2="339" y2="344"/>
      <line x1="166" y1="332" x2="285" y2="457"/>
      <line x1="166" y1="332" x2="114" y2="462"/>
      <line x1="166" y1="332" x2="59" y2="344"/>
    </g>
    <circle cx="166" cy="332" r="80" fill="#fff" stroke="#4a93d3" stroke-width="10"/>
    <circle cx="166" cy="332" r="62" fill="#2f8fd6"/>
    <use href="#icon-table" x="126" y="300" width="80" height="64"/>
    <g fill="#fff" stroke="#4a93d3" stroke-width="6">
      <circle cx="142" cy="225" r="30"/><circle cx="273" cy="232" r="30"/>
      <circle cx="339" cy="344" r="30"/><circle cx="285" cy="457" r="30"/>
      <circle cx="114" cy="462" r="30"/><circle cx="59" cy="344" r="30"/>
    </g>
    <g fill="#4a93d3" font-family="Arimo, Arial, sans-serif" font-size="32" font-weight="700" text-anchor="middle">
      <text x="142" y="236">?</text><text x="273" y="243">?</text>
      <text x="339" y="355">?</text><text x="285" y="468">?</text>
      <text x="114" y="473">?</text><text x="59" y="355">?</text>
    </g>
    <g fill="none" stroke="#4a93d3" stroke-width="16" stroke-linecap="round">
      <path d="M166,505 C140,800 300,990 515,1002" marker-end="url(#arrow-head)"/>
      <path d="M395,330 C330,560 470,650 600,600" marker-end="url(#arrow-head)"/>
      <path d="M1030,250 Q960,120 840,150" marker-end="url(#arrow-head)"/>
      <path d="M900,1040 C940,1115 1085,1100 1112,975" marker-end="url(#arrow-head)"/>
    </g>
    <g fill="#fff" stroke="#4a93d3" stroke-width="8">
      <circle cx="937" cy="308" r="66"/><circle cx="1103" cy="308" r="66"/>
      <circle cx="937" cy="462" r="66"/><circle cx="1103" cy="462" r="66"/>
    </g>
    <g fill="#3f8fd4">
      <circle cx="937" cy="308" r="52"/><circle cx="1103" cy="462" r="52"/>
    </g>
    <use href="#icon-pot" x="900" y="276" width="74" height="66"/>
    <use href="#icon-cup" x="1079" y="276" width="48" height="64"/>
    <use href="#icon-table" x="895" y="432" width="84" height="66"/>
    <use href="#icon-table" x="1061" y="430" width="84" height="66"/>
    <g fill="#fff" stroke="#b9cbe0" stroke-width="4">
      <circle cx="700" cy="742" r="50"/><circle cx="806" cy="742" r="50"/>
      <circle cx="913" cy="742" r="50"/><circle cx="1020" cy="742" r="50"/>
      <circle cx="1127" cy="742" r="50"/>
    </g>
    <g fill="#3f8fd4">
      <circle cx="700" cy="742" r="40"/><circle cx="806" cy="742" r="40"/>
      <circle cx="913" cy="742" r="40"/><circle cx="1020" cy="742" r="40"/>
      <circle cx="1127" cy="742" r="40"/>
    </g>
    <g fill="#fff">
      <circle cx="700" cy="742" r="22"/>
      <circle cx="806" cy="742" r="22" fill="none" stroke="#fff" stroke-width="5"/>
      <rect x="899" y="720" width="28" height="44" rx="3"/>
      <polygon points="1020,716 1027,732 1044,728 1033,742 1044,756 1027,752 1020,768 1013,752 996,756 1007,742 996,728 1013,732"/>
      <text x="1127" y="756" font-family="Arimo, Arial, sans-serif" font-size="40" font-weight="700" text-anchor="middle">$</text>
    </g>
  </svg>

  <div class="step-num" style="left:22px;top:76px">1</div>
  <div class="step-label" style="left:62px;top:83px;width:270px">Compare proposed new concept to market</div>

  <div class="step-num" style="left:413px;top:466px">2</div>
  <div class="step-label" style="left:464px;top:486px;width:224px">iteratively refine the new concept</div>

  <div class="step-num" style="left:606px;top:968px">3</div>
  <div class="step-label" style="left:664px;top:972px;width:304px">create a business model for the new concept</div>

  <div class="step-num" style="left:742px;top:562px">4</div>
  <div class="step-label" style="left:797px;top:569px;width:384px">Create the blueprints for the components: Menus, Drinks, Floor Plans, Brand Concept</div>

  <div class="step-num" style="left:385px;top:818px">4</div>
  <div class="step-label" style="left:431px;top:823px;width:750px">Also includes blueprints to make it work: Operational Procedures; Sourcing; Staffing models, with Role Descriptions and Hierarchies; Sales and Marketing Plans, and Financial models.)</div>

  <div class="step-num" style="left:723px;top:44px">5</div>
  <div class="step-label" style="left:773px;top:47px;width:408px">Using the Blueprints, set up the operation to deliver the new dining concept consistently and elegantly.</div>
</section>

<footer class="site-footer">
  <div class="roles">Chef - Entrepreneur - Designer<br>Creative Director - Connector of People</div>
  <div class="divider"></div>
  <div class="contacts">
    <span><svg width="16" height="16" viewBox="0 0 24 24"><path fill="#fff" d="M6.6 10.8a15 15 0 006.6 6.6l2.2-2.2c.3-.3.7-.4 1-.2 1.1.4 2.3.6 3.6.6.6 0 1 .4 1 1V20c0 .6-.4 1-1 1A17 17 0 013 4c0-.6.4-1 1-1h3.5c.6 0 1 .4 1 1 0 1.3.2 2.5.6 3.6.1.3 0 .7-.2 1z"/></svg>+61 400 555 218</span>
    <span><svg width="18" height="14" viewBox="0 0 24 18"><rect x="1" y="1" width="22" height="16" rx="2" fill="#fff"/><path d="M2 2l10 8 10-8" fill="none" stroke="#3d8fd1" stroke-width="2"/></svg>glen@glenmarbury.com.au</span>
    <span><svg width="14" height="14" viewBox="0 0 24 24"><circle cx="12" cy="12" r="11" fill="#fff"/><circle cx="12" cy="10" r="4" fill="#3d8fd1"/></svg>www.glenmarbury.com.au</span>
  </div>
</footer>

</body>
</html>
```